Re-launching marine insurance adjusting company - looking for energy

I am a sole practitioner specializing in the profession of average adjusting. There is an on-line brochure at www.rkbtnova.com I am one of only a handful of specialists in this field and I enjoy a fair amount of name recognition, domestically in the US and internationally. My principal markets are the US, the London and Scandinavian insurance markets and shipowners and insurers in Latin America.
The business is a mixture of law, accounting and insurance and my clientele relies on a time-sensitive and accurate work-product, clearly stating an insurance company's liability for a given claim. The identity needs to project gravitas rather than flash.
Since 1998 I have traded as "The Halloway Company" but have also attempted to establish the name RKBNOVA.com so that people would visit my website.
I want to implement a single identity across my stationery, business cards and website. I have come to see "The Halloway Company" as rather fatuous, since there is no company, it is just me. The Internet domain RKBNOVA is long-established and I would be reluctant to change it. I have considered trading as simply Marcus T Halloway, MTH, RKBNOVA or attempting to come up with a name that could be abbreviated to MTH, e.g. M Halloway Trelantics - but I can't find a suitable word for the second S.
Logo-wise, I have considered a stylized MTH or RKBNOVA redolent of waves of the sea. A nautical theme embodying a cargo ship, navigational beacon or lighthouse might be appropriate but these tend to be hackneyed.
I have attached a card that I mocked up at Pix, connoting stacking up numbers, which I really like, but I think it is too cryptic for people in most insurance companies, who don't particularly think laterally or they wouldn't work in marine insurance, and the card that I use currently, which I intended to be understated, but in fact it states nothing.
I have also attached my current letterhead, to demonstrate how I really need help.
Finally, I have attached a credentials sheet, to attempt to establish how narrow and deep is the professional niche that I occupy.
What I am looking to implement is a single logo, font, them and color scheme to use across my website, letterhead and business cards.
Over to the Sketch Guild...
Target Market(s)
Ship owners and insurance companies
Industry/Entity Type
Accounting

```html
<!DOCTYPE html>
<html lang="en">
<head>
<meta charset="utf-8">
<title>RKBNOVA.com – Identity Set</title>
<link href="https://fonts.googleapis.com/css2?family=Arimo&family=Oswald:wght@400;600&display=swap" rel="stylesheet">
<style>
  :root {
    --canvas: #ffffff;
    --paper-edge: #efefed;
    --paper: #ffffff;
    --brand-orange: #f07a2c;
    --ink-brown: #8a3e17;
    --sketch-brown: #a86a45;
    --sketch-light: #f3e6dc;
    --label: #111111;
  }
  * { margin: 0; padding: 0; box-sizing: border-box; }
  html, body { width: 1200px; height: 998px; overflow: hidden; background: var(--canvas); }
  body { position: relative; font-family: "Oswald", sans-serif; color: var(--ink-brown); }

  .section-label {
    position: absolute;
    font-family: "Arimo", Arial, sans-serif;
    font-size: 44px;
    color: var(--label);
    line-height: 1;
  }
  .label-letterhead { left: 15px; top: 84px; }
  .label-logo { left: 656px; top: 150px; }
  .label-card { left: 662px; top: 554px; }

  .sheet {
    position: absolute;
    background: var(--paper-edge);
  }
  .sheet-inner {
    position: absolute;
    background: var(--paper);
    border-radius: 14px;
    box-shadow: 0 0 12px 6px var(--paper);
  }

  .illustration {
    position: absolute;
    background: radial-gradient(ellipse at 30% 55%, var(--sketch-light) 0%, rgba(243,230,220,0.5) 55%, rgba(255,255,255,0) 80%);
    border-bottom: 2px solid rgba(168,106,69,0.35);
  }

  .brand-name {
    position: absolute;
    font-weight: 600;
    color: var(--brand-orange);
    line-height: 1;
    white-space: nowrap;
  }
  .person-name {
    position: absolute;
    font-weight: 400;
    color: var(--ink-brown);
    line-height: 1;
    white-space: nowrap;
  }
  .contact {
    position: absolute;
    font-size: 12px;
    line-height: 1.95;
    color: var(--ink-brown);
    white-space: nowrap;
  }
  .address {
    position: absolute;
    font-weight: 400;
    color: var(--ink-brown);
    white-space: nowrap;
    line-height: 1;
    word-spacing: 2px;
  }

  /* Letterhead */
  .letterhead { left: 14px; top: 143px; width: 578px; height: 819px; }
  .letterhead .sheet-inner { left: 26px; top: 24px; width: 526px; height: 770px; }
  .letterhead .illustration { left: 36px; top: 25px; width: 300px; height: 142px; }
  .letterhead .brand-name { left: 121px; top: 63px; font-size: 27px; }
  .letterhead .person-name { left: 176px; top: 92px; font-size: 22px; }
  .letterhead .contact { left: 409px; top: 70px; }
  .letterhead .address { left: 51px; top: 177px; font-size: 22px; }

  /* Logo */
  .logo-lockup { position: absolute; left: 650px; top: 250px; width: 445px; height: 215px; }
  .logo-lockup .illustration { left: 0; top: 5px; width: 440px; height: 205px; }
  .logo-lockup .brand-name { left: 148px; top: 55px; font-size: 38px; }
  .logo-lockup .person-name { left: 228px; top: 96px; font-size: 32px; }

  /* Business card */
  .business-card { left: 659px; top: 617px; width: 456px; height: 291px; }
  .business-card .sheet-inner { left: 14px; top: 18px; width: 428px; height: 256px; }
  .business-card .illustration { left: 12px; top: 28px; width: 440px; height: 220px; }
  .business-card .brand-name { right: 32px; top: 33px; font-size: 24px; }
  .business-card .person-name { right: 32px; top: 61px; font-size: 22px; }
  .business-card .contact-phone { left: 188px; top: 102px; }
  .business-card .contact-web { left: 304px; top: 102px; }
  .business-card .address { left: 26px; top: 248px; font-size: 20px; }
</style>
</head>
<body>

  <h2 class="section-label label-letterhead">Letterhead</h2>
  <section class="sheet letterhead">
    <div class="sheet-inner"></div>
    <div class="illustration" role="img" aria-label="Hand-sketched lighthouse on a rocky shore with sea waves, in brown ink"></div>
    <div class="brand-name">RKBNOVA.com</div>
    <div class="person-name">Marcus T Halloway</div>
    <div class="contact">
      Tel: (212) 555 0147<br>
      Fax: (212) 555 0192<br>
      Website: www.rkbnova.com<br>
      Email: &nbsp; info@rkbnova.com
    </div>
    <div class="address">27 Harbor Point Road, &nbsp;New York, &nbsp;NY 10031, USA</div>
  </section>

  <h2 class="section-label label-logo">Logo</h2>
  <section class="logo-lockup">
    <div class="illustration" role="img" aria-label="Hand-sketched lighthouse on a rocky shore with sea waves, in brown ink"></div>
    <div class="brand-name">RKBNOVA.com</div>
    <div class="person-name">Marcus T Halloway</div>
  </section>

  <h2 class="section-label label-card">Business card</h2>
  <section class="sheet business-card">
    <div class="sheet-inner"></div>
    <div class="illustration" role="img" aria-label="Hand-sketched lighthouse on a rocky shore with sea waves, in brown ink"></div>
    <div class="brand-name">RKBNOVA.com</div>
    <div class="person-name">Marcus T Halloway</div>
    <div class="contact contact-phone">
      Tel: &nbsp;(212) 555 0147<br>
      Fax: (212) 555 0192
    </div>
    <div class="contact contact-web">
      Website: www.rkbnova.com<br>
      Email: &nbsp;info@rkbnova.com
    </div>
    <div class="address">27 Harbor Point Road, &nbsp;New York, &nbsp;NY 10031, USA</div>
  </section>

</body>
</html>
```